Curtain and Blind Manufacturers - Retail Ecommerce All Pages

To Design a high converting website design for and improve on the domain www.velcourt-weaves.co.uk.

Generally it is improvements on what already exists, the core layout is functional and strong. Needs to have the header mobile responsive. Core elements for each page and clear content.

Current header is good just needs modernising and needs to work well on mobile. Need a way of having a mixture of categories and advice where necessary.

Pages and detailing required.
Home - Great Imagery for the sections. Category specific. A good product offering. So Call to product. Potentially straight to our best selling products. Not in a slider but in a straight forward grid. A nice simlar design to competitors in my space. shutterly4u, my own website. also i like websites like nessa mattresses, harrowdens.co.uk needs to be simple with clear direction for the customer particularly on mobile to get them to what we do quickly. EG curtains, blinds etc

Inner pages

Category Top Filters
https://www.velcourt-weaves.co.uk/flame-retardant/curtains

Category Side bar filters

Category Mobile with Off Canvas Filters

Product - Fabric
https://www.velcourt-weaves.co.uk/tovra-flame-retardant-curtain-fabric.html

Product - Curtains - https://www.velcourt-weaves.co.uk/tovra-fr-curtains.html

Product - Blinds
Cart
Checkout
Slide in Cart
Slide in Filters
General Content Page
About

```html
<!DOCTYPE html>
<html lang="en">
<head>
<meta charset="utf-8">
<title>Velcourt Weaves – Flame Retardant & Contract Furnishings</title>
<link href="https://fonts.googleapis.com/css2?family=Inter:wght@400;500;600;700&family=Urbanist:wght@500;600;700&display=swap" rel="stylesheet">
<style>
:root{
  --maroon:#74222d;
  --maroon-dark:#4e121b;
  --red:#c8202e;
  --ink:#1d1d1f;
  --muted:#555;
  --line:#e3e3e3;
  --soft:#f3f3f3;
  --footer:#2f2f2f;
  --white:#fff;
}
*{box-sizing:border-box;margin:0;padding:0}
html,body{width:1200px;height:4977px;overflow:hidden}
body{position:relative;font-family:"Inter",sans-serif;color:var(--ink);background:var(--white)}
.abs{position:absolute}
svg{display:block}

/* top bar */
.topbar{left:0;top:0;width:1200px;height:33px;background:var(--maroon);color:#fff;font-size:10px;font-weight:500}
.topbar .note{left:66px;top:11px}
.topbar .pay{right:110px;top:10px;display:flex;gap:4px}
.topbar .pay span{width:26px;height:14px;background:#fff;border-radius:2px}
.topbar .icons{right:62px;top:8px;display:flex;gap:14px}

/* header */
.header{left:0;top:33px;width:1200px;height:89px;border-bottom:1px solid var(--line)}
.phone{left:66px;top:33px;display:flex;align-items:center;gap:8px;font-size:17px;color:var(--ink)}
.search{left:226px;top:33px}
.brand{left:522px;top:22px;display:flex;align-items:center;gap:8px}
.brand .mark{width:30px;height:30px;background:var(--red)}
.brand .name{font-family:"Urbanist",sans-serif;font-weight:700;font-size:19px;color:var(--red);line-height:1}
.brand .tag{font-size:7px;letter-spacing:1px;color:var(--ink);margin-top:3px;font-weight:600}
.cart{left:924px;top:30px}
.quote-btn{left:976px;top:24px;width:160px;height:40px;background:var(--red);color:#fff;font-size:12px;font-weight:600;display:flex;align-items:center;justify-content:center;border-radius:3px}

/* nav */
.nav{left:0;top:122px;width:1200px;height:73px;display:flex;justify-content:center;gap:38px;align-items:center;font-size:13px;font-weight:500}
.nav span::after{content:"";display:inline-block;width:5px;height:5px;border-right:1.3px solid #444;border-bottom:1.3px solid #444;transform:rotate(45deg);margin-left:8px;position:relative;top:-3px}

/* hero */
.hero{left:0;top:195px;width:1200px;height:501px;background:radial-gradient(ellipse at 70% 30%,#9a3440 0%,#74222d 40%,#4a1119 100%)}
.hero h1{left:62px;top:110px;width:640px;font-family:"Urbanist",sans-serif;font-weight:500;font-size:33px;line-height:50px;color:#fff}
.hero .shop{left:62px;top:284px;width:316px;height:43px;background:var(--red);color:#fff;font-size:12px;font-weight:600;display:flex;align-items:center;justify-content:center;gap:10px;border-radius:3px}
.trusted{left:66px;top:449px;display:flex;align-items:center;gap:26px}
.trusted .pill{border:1.3px solid #fff;border-radius:20px;padding:7px 14px;color:#fff;font-size:9px;font-weight:700}
.trusted .badge{height:18px;background:rgba(255,255,255,.75);border-radius:2px}
.form{left:769px;top:52px;width:367px;height:449px;background:#fff}
.form h3{text-align:center;font-size:16px;font-weight:700;margin-top:26px}
.form p{text-align:center;font-size:10px;color:#888;line-height:16px;margin:8px 50px 0}
.form .field{margin:12px 32px 0;height:42px;border:1px solid var(--line);border-radius:3px;display:flex;align-items:center;gap:10px;padding:0 12px;font-size:10px;color:#666}
.form .field b{color:var(--red);font-weight:500}
.form .area{height:76px;align-items:flex-start;padding-top:14px;line-height:17px}
.form .send{position:absolute;left:0;bottom:0;width:367px;height:74px;background:var(--red);color:#fff;font-size:12px;font-weight:700;display:flex;align-items:center;justify-content:center;gap:8px}

/* usp row */
.usp{top:738px;height:66px;width:342px;border:1.5px solid var(--red);border-radius:4px;display:flex;align-items:center;justify-content:center;gap:10px;color:var(--red);font-size:12px;font-weight:600}
.usp.fill{background:#fbe9ea}
.stars{display:flex;gap:2px}
.stars i{width:14px;height:14px;background:#1a9d57}

/* category hero tiles */
.cat{top:846px;width:400px;height:406px;color:#fff}
.cat .num{position:absolute;left:32px;top:38px;font-family:"Urbanist",sans-serif;font-size:32px;font-weight:700}
.cat .lbl{position:absolute;left:32px;bottom:58px;font-size:31px;font-weight:600}
.cat .lbl.low{bottom:38px}
.cat .more{position:absolute;left:32px;bottom:32px;font-size:13px}

/* product grid */
.tile{width:334px;height:312px;color:#fff}
.tile .lbl{position:absolute;left:25px;bottom:38px;font-size:17px;font-weight:600}
.tile .lbl.up{bottom:50px}
.tile .more{position:absolute;left:25px;bottom:26px;font-size:13px}

/* intro */
.intro{left:150px;top:2430px;width:900px;text-align:center}
.intro h2{font-size:24px;font-weight:700}
.intro p{font-size:11px;line-height:20px;color:#444;margin-top:18px}
.feat{width:518px}
.feat .img{height:292px}
.feat h4{font-size:16px;font-weight:700;margin-top:42px}
.feat p{font-size:12.5px;line-height:25px;color:#333;margin-top:10px}
.feat a{color:var(--red);text-decoration:underline}

/* about band */
.about{left:0;top:3628px;width:1200px;height:418px;background:var(--soft);text-align:center}
.about h2{font-size:24px;font-weight:700;margin-top:72px}
.about p{font-size:11px;line-height:20px;color:#444;margin:24px 160px 0}
.about p+p{margin-top:16px}
.about a{color:var(--red);text-decoration:underline}

/* reviews */
.rev{top:4131px;height:206px;background:#f6f6f6;text-align:center;padding:24px 18px}
.rev .top{display:flex;justify-content:center;align-items:center;gap:10px;font-size:10px;color:#888}
.rev .top .stars i{width:12px;height:12px}
.rev h5{font-size:12px;font-weight:700;margin-top:14px;line-height:18px}
.rev p{font-size:11px;line-height:19px;color:#444;margin-top:8px}
.rev .who{font-size:11px;margin-top:6px}
.rev .who b{font-weight:700}
.summary h5{font-size:24px;font-weight:500;margin-top:12px}
.summary .stars{justify-content:center;margin-top:14px;gap:4px}
.summary .stars i{width:28px;height:28px}
.dots{left:562px;top:4362px;display:flex;gap:8px}
.dots i{width:38px;height:4px;background:#ddd}
.dots i:first-child{background:var(--red)}

/* footer */
.footer{left:0;top:4453px;width:1200px;height:524px;background:var(--footer);color:#ddd}
.footer h6{position:absolute;top:74px;font-size:14px;font-weight:700;color:#fff}
.footer ul{position:absolute;top:118px;list-style:none;font-size:12.5px;line-height:32px;color:#ccc}
.footer ul li::before{content:"›";margin-right:10px;color:#ccc}
.footer .contact{position:absolute;left:900px;top:118px;font-size:12.5px;line-height:21px;color:#ccc}
.footer .fbrand{position:absolute;left:66px;top:395px;display:flex;align-items:center;gap:8px}
.footer .fbrand .mark{width:30px;height:30px;background:var(--red)}
.footer .fbrand .name{font-family:"Urbanist",sans-serif;font-weight:700;font-size:19px;color:var(--red)}
.footer .social{position:absolute;left:66px;top:458px;display:flex;gap:14px}
.footer .social i{width:44px;height:44px;border:1.5px solid #fff;border-radius:50%}
.footer .cards{position:absolute;right:64px;top:400px;display:flex;gap:4px}
.footer .cards span{width:40px;height:26px;background:#fff;border-radius:3px}
.footer .copy{position:absolute;right:64px;top:464px;font-size:12px;color:#ccc}
.chat{left:1135px;top:4725px;width:52px;height:52px;border-radius:50%;background:var(--red);display:flex;align-items:center;justify-content:center}
</style>
</head>
<body>

<div class="abs topbar">
  <span class="abs note">FREE DELIVERY £250 UK EX SHI&amp;I</span>
  <div class="abs pay"><span></span><span></span><span></span><span></span></div>
  <div class="abs icons">
    <svg width="14" height="14" viewBox="0 0 14 14" fill="none" stroke="#fff" stroke-width="1.3"><circle cx="7" cy="4.5" r="3"/><path d="M1.5 13c.8-3 3-4.5 5.5-4.5s4.7 1.5 5.5 4.5"/></svg>
    <svg width="14" height="14" viewBox="0 0 14 14" fill="none" stroke="#fff" stroke-width="1.3"><circle cx="7" cy="7" r="5.5"/><path d="M3 7h8M7 3v8"/></svg>
  </div>
</div>

<header class="abs header">
  <div class="abs phone">
    <svg width="16" height="16" viewBox="0 0 16 16" fill="none" stroke="#c8202e" stroke-width="1.5"><path d="M3 1.5h3l1.5 4-2 1.2a9 9 0 0 0 3.8 3.8l1.2-2 4 1.5v3a1.5 1.5 0 0 1-1.5 1.5A13 13 0 0 1 1.5 3 1.5 1.5 0 0 1 3 1.5z"/></svg>
    0117 4960218
  </div>
  <svg class="abs search" width="20" height="20" viewBox="0 0 20 20" fill="none" stroke="#c8202e" stroke-width="1.7"><circle cx="8.5" cy="8.5" r="6.5"/><path d="M13.5 13.5l5 5"/></svg>
  <div class="abs brand">
    <span class="mark"></span>
    <div><div class="name">VELCOURT WEAVES</div><div class="tag">CURTAINS · BLINDS · FABRICS</div></div>
  </div>
  <svg class="abs cart" width="26" height="26" viewBox="0 0 26 26" fill="none" stroke="#c8202e" stroke-width="1.6"><path d="M2 4h4l3 12h12l3-9H8"/><circle cx="11" cy="21" r="1.6"/><circle cx="19" cy="21" r="1.6"/><circle cx="20" cy="20" r="4" fill="#2aa35a" stroke="none"/></svg>
  <div class="abs quote-btn">GET QUICK QUOTE!</div>
</header>

<nav class="abs nav">
  <span>Curtains</span><span>Blinds</span><span>Fabrics</span><span>Flame Retardant</span><span>Tracks</span><span>Poles</span><span>Bedding &amp; Linens</span><span>Furniture</span>
</nav>

<section class="abs hero" role="img" aria-label="Draped deep red flame retardant curtain fabric">
  <h1 class="abs">Flame Retardant &amp; Contract Specialists.Contact today – Supply Only OR Manufacture to Installation</h1>
  <div class="abs shop">Shop Online For Contract Furnishings
    <svg width="14" height="10" viewBox="0 0 14 10" fill="none" stroke="#fff" stroke-width="1.5"><path d="M0 5h12M8 1l4 4-4 4"/></svg>
  </div>
  <div class="abs trusted">
    <span class="pill">SUPPLYING &amp; TRUSTED BY</span>
    <span class="badge" style="width:54px"></span>
    <span class="badge" style="width:80px"></span>
    <span class="badge" style="width:84px"></span>
    <span class="badge" style="width:58px"></span>
    <span class="badge" style="width:62px"></span>
  </div>
  <form class="abs form">
    <h3>Quick Quote &amp; Free Sample Requests</h3>
    <p>SAVE TIME - Send your project requirements, large or small. Sample Lists etc</p>
    <div class="field"><svg width="12" height="12" viewBox="0 0 14 14" fill="none" stroke="#555" stroke-width="1.3"><circle cx="7" cy="4.5" r="3"/><path d="M1.5 13c.8-3 3-4.5 5.5-4.5s4.7 1.5 5.5 4.5"/></svg>Your name <b>*</b></div>
    <div class="field"><svg width="13" height="11" viewBox="0 0 13 11" fill="none" stroke="#555" stroke-width="1.3"><rect x=".7" y=".7" width="11.6" height="9.6"/><path d="M.7 1l5.8 5 5.8-5"/></svg>Your email <b>*</b></div>
    <div class="field"><svg width="12" height="12" viewBox="0 0 16 16" fill="none" stroke="#555" stroke-width="1.5"><path d="M3 1.5h3l1.5 4-2 1.2a9 9 0 0 0 3.8 3.8l1.2-2 4 1.5v3a1.5 1.5 0 0 1-1.5 1.5A13 13 0 0 1 1.5 3 1.5 1.5 0 0 1 3 1.5z"/></svg>Enter your number <b>*</b></div>
    <div class="field area">EXAMPLE: Looking for roller blinds &amp; curtains. Track width 150cm x 240cm Drop <b>*</b></div>
    <div class="send"><svg width="14" height="14" viewBox="0 0 14 14" fill="none" stroke="#fff" stroke-width="1.3"><path d="M7 1l1.8 3.8 4.2.5-3.1 2.9.8 4.1L7 10.3l-3.7 2 .8-4.1L1 5.3l4.2-.5z"/></svg>GET QUICK QUOTE! / SEND MESSAGE NOW</div>
  </form>
</section>

<div class="abs usp" style="left:66px;color:var(--ink)">
  <span class="stars"><i></i><i></i><i></i><i></i><i></i></span><span style="font-size:11px">Reviewly</span>
</div>
<div class="abs usp fill" style="left:431px;width:340px">
  <svg width="18" height="18" viewBox="0 0 18 18" fill="none" stroke="#c8202e" stroke-width="1.3" stroke-dasharray="2 2"><rect x="1" y="1" width="16" height="16"/></svg>FREE FABRIC SAMPLES
</div>
<div class="abs usp" style="left:794px">
  <svg width="16" height="16" viewBox="0 0 14 14" fill="none" stroke="#c8202e" stroke-width="1.2"><path d="M7 1l1.8 3.8 4.2.5-3.1 2.9.8 4.1L7 10.3l-3.7 2 .8-4.1L1 5.3l4.2-.5z"/></svg>NATIONWIDE INSTALLATION
</div>

<a class="abs cat" style="left:0;background:linear-gradient(160deg,#eeeeec,#c9c6c1)" role="img" aria-label="Bright room with white sheer curtains">
  <span class="num">01.</span><span class="lbl">Curtains</span><span class="more">Shop Now →</span>
</a>
<a class="abs cat" style="left:400px;background:linear-gradient(150deg,#7d3a5c,#c8452c 40%,#d8a23a 60%,#6a5a48)" role="img" aria-label="Stack of colourful fabric swatches">
  <span class="num">02.</span><span class="lbl low">Fabrics</span>
</a>
<a class="abs cat" style="left:800px;background:linear-gradient(160deg,#e6e4e1,#a9a39b)" role="img" aria-label="Kitchen window with white venetian blinds">
  <span class="num">03.</span><span class="lbl low">Blinds</span>
</a>

<a class="abs tile" style="left:66px;top:1337px;background:linear-gradient(160deg,#a9bccb,#5c7892)" role="img" aria-label="Blue flame retardant curtains in a living room">
  <span class="lbl up">Flame Retardant Curtains</span><span class="more">Shop Now →</span></a>
<a class="abs tile" style="left:435px;top:1337px;background:linear-gradient(160deg,#3c6670,#1f3b43)" role="img" aria-label="Teal stage curtains"><span class="lbl">Stage / Theatre Curtains</span></a>
<a class="abs tile" style="left:802px;top:1337px;background:linear-gradient(160deg,#e8e2da,#a89482)" role="img" aria-label="White flame retardant bedding"><span class="lbl">Flame Retardant Bedding</span></a>
<a class="abs tile" style="left:66px;top:1683px;background:linear-gradient(160deg,#b08a74,#6e5548)" role="img" aria-label="Folded fire resistant curtain fabrics"><span class="lbl">Fire Resistant Curtain Fabrics</span></a>
<a class="abs tile" style="left:435px;top:1683px;background:linear-gradient(160deg,#f0ebe2,#bdb3a2)" role="img" aria-label="Roller blind chain mechanism"><span class="lbl">Fire Retardant Roller Blinds</span></a>
<a class="abs tile" style="left:802px;top:1683px;background:linear-gradient(90deg,#d9dde2,#3f86d0 40%,#2f6fb8 70%,#d9dde2)" role="img" aria-label="Blue hospital cubicle curtains on track"><span class="lbl">Cubicle Curtains And Tracks</span></a>
<a class="abs tile" style="left:66px;top:2029px;background:linear-gradient(160deg,#f1eeeb,#c9c2bb)" role="img" aria-label="Hands hanging white curtain on track"><span class="lbl">Curtain Tracks</span></a>
<a class="abs tile" style="left:435px;top:2029px;background:linear-gradient(160deg,#5a5753,#232120)" role="img" aria-label="Office with metal venetian blinds"><span class="lbl">Metal Venetian Blinds</span></a>
<a class="abs tile" style="left:802px;top:2029px;background:linear-gradient(160deg,#e2ded8,#b39a7c)" role="img" aria-label="White vertical blinds over wooden floor"><span class="lbl">Vertical Blinds</span></a>

<section class="abs intro">
  <h2>Flame Retardant &amp; Contract Furnishing Specialists</h2>
  <p>Velcourt Weaves supply the UK with soft furnishings for commercial environments certified to <b>British and International Flame Retardant Standards</b>. Including BS5867, BS7175, BS5852, IMO M1 &amp; B1. Velcourt Weaves has been set up to supply the UK and the world with a superior range of contract furnishings. From manufacture to installation. We are an NCS certified supplier and work supplying hotels, care homes, schools and more. Our company is based in the United Kingdom. We look forward to working with you to supply the very best <b>contract curtains, blinds, stage curtains and also cubicle curtains and tracks.</b></p>
</section>

<article class="abs feat" style="left:66px;top:2602px">
  <div class="img" style="background:linear-gradient(160deg,#e6e4df,#8e8b86)" role="img" aria-label="Sewing machines in a UK workshop"></div>
  <h4>UK MANUFACTURED</h4>
  <p>All our curtains and blinds are made here in the United Kingdom. We believe in quality and buying British where possible, so we make all of our made to measure soft furnishings including; curtains, blinds, accessories here in the UK.</p>
</article>
<article class="abs feat" style="left:618px;top:2602px">
  <div class="img" style="background:#1f63b5" role="img" aria-label="Health service supplier badge"></div>
  <h4>NCS CERTIFIED SUPPLIER</h4>
  <p>Velcourt Weaves are registered NCS suppliers working on small projects for individual medical practices as well as full <b>hospital</b> contract for <a>cubicle curtain rails</a></p>
</article>
<article class="abs feat" style="left:66px;top:3066px">
  <div class="img" style="background:linear-gradient(180deg,#f2f0ed 0%,#e8e4df 30%,#e9c7c4 35%,#dfb8b5 100%)" role="img" aria-label="Pink cassette roller blind in a window"></div>
  <h4>Cassette Roller Blinds</h4>
  <p>A <a>cassette blackout roller blind</a> manufacturer who manufacturers the very best roller blinds for commercial and domestic situations. Our cassette roller blinds are of the highest quality and made to last with a 10 year guarantee. Speak with the team to get a quote for your cassette blackout blinds. Premium Cassette roller blinds with side channels</p>
</article>
<article class="abs feat" style="left:618px;top:3066px">
  <div class="img" style="background:linear-gradient(90deg,#2c2c2e 0%,#3a3a3c 20%,#d6d0c8 40%,#e6e2dc 100%)" role="img" aria-label="Bedroom with dark soundproof curtains"></div>
  <h4>Soundproof Curtains</h4>
  <p>A <a>Soundproof curtain</a> manufacturer. We only use certified and tested products that deliver the highest acoustic absorption with an 11db sound proofing. All tested and certified products that work to soundproof your rooms with curtains. Block unwanted noise from your space and also improve room acoustics with acoustic absorption.</p>
</article>

<section class="abs about">
  <h2>Velcourt Weaves - Curtains, Blinds, Fabric</h2>
  <p>Velcourt Weaves has been set up to supply the UK and the world with a superior range of <b>curtain fabrics</b> and <b>made to measure curtains</b>. Ensuring that all products are certified to the necessary British and European flame retardant standards. Our flame retardant fabrics are manufactured into excellent curtains, blinds and soft furnishings in our factories across the UK. Purchase your <b>contract curtains</b> and soft furnishings from a UK company with a large buying power that can offer the full service from design, manufacture and installation of contract furnishings. The team at Velcourt Weaves will ensure that you can get the project completed on time and on budget with made to measure curtains manufactured in as little as <u><b>15-20 working days</b></u>.</p>
  <p>The products Velcourt Weaves offer to the NCS include hospital <a>cubicle curtain rails</a>, <a>cubicle curtains</a>. The team will work with you to get the very commercial certified flame retardant products for your business.</p>
  <p>Velcourt Weaves supply businesses from all sectors including; <b>Care, Hospitality and Education</b>. Working with at risk areas within care homes and schools, Velcourt Weaves understand the risks and ensure that the products are all ideally suited both in design and in performance. buy Velcourt Weaves from a UK business that can deliver quickly and with excellent quality <b>contract furnishings</b></p>
</section>

<div class="abs rev summary" style="left:66px;width:243px">
  <h5>Excellent</h5>
  <div class="stars"><i></i><i></i><i></i><i></i><i></i></div>
  <p style="font-size:10px;color:#777;margin-top:10px">Based on <u>1,675 reviews</u></p>
  <div style="display:flex;justify-content:center;align-items:center;gap:6px;margin-top:14px;font-size:16px;font-weight:600"><i style="width:16px;height:16px;background:#1a9d57;display:inline-block"></i>Reviewly</div>
</div>
<div class="abs rev" style="left:325px;width:276px">
  <div class="top"><span class="stars"><i></i><i></i><i></i><i></i><i></i></span>Verified</div>
  <h5>The agent I spoke to in an online chat...</h5>
  <p>The agent I spoke to in an online chat was very helpful, answering all my questi...</p>
  <div class="who"><b>Maria</b>, 6 days ago</div>
</div>
<div class="abs rev" style="left:618px;width:277px">
  <div class="top"><span class="stars"><i></i><i></i><i></i><i></i><i></i></span>Verified</div>
  <h5>Great product, very reasonable price.</h5>
  <p>The curtain track arrived quickly and was great quality despite the very reasona...</p>
  <div class="who"><b>Maria</b>, 6 days ago</div>
</div>
<div class="abs rev" style="left:912px;width:276px">
  <div class="top"><span class="stars"><i></i><i></i><i></i><i></i><i></i></span>Verified</div>
  <h5>Good quality</h5>
  <p>Great response, quickly delivery, fab quality of the fabric.</p>
  <div class="who"><b>Maria</b>, 6 days ago</div>
</div>
<div class="abs dots"><i></i><i></i><i></i></div>

<footer class="abs footer">
  <h6 style="left:75px">USEFUL LINKS</h6>
  <ul style="left:75px"><li>About Us</li><li>FAQ - Frequently Asked Questions</li><li>Curtain and Blind Installation Nationwide</li><li>How to Measure for Curtains and Blinds</li><li>Terms and Conditions</li><li>Privacy Policy</li></ul>
  <ul style="left:396px"><li>Blog</li><li>Delivery &amp; Shipping Information</li><li>Returns &amp; Cancellation</li><li>Client Reviews</li><li>Contact Us</li><li>Charity</li></ul>
  <h6 style="left:665px">OUR PRODUCTS</h6>
  <ul style="left:665px;top:112px;line-height:25px"><li>Flame Retardant Curtains</li><li>Fire Resistant Blinds</li><li>Made to Measure Curtains</li><li>Acoustic Curtains</li><li>Curtain Fabrics</li><li>Curtain Poles</li><li>Curtain Tracks</li></ul>
  <h6 style="left:900px">CONTACT US</h6>
  <div class="contact">T : 0117 496 0731<br>Mon - Fri 9am - 5pm<br><br>Orlen Trading LTD<br>Velcourt Weaves<br>Front Office, Unit 7 Kestrel Park Road<br>Bristol, BS99 1ZZ</div>
  <div class="fbrand"><span class="mark"></span><span class="name">VELCOURT WEAVES</span></div>
  <div class="social"><i></i><i></i><i></i><i></i></div>
  <div class="cards"><span></span><span></span><span></span><span></span><span></span></div>
  <div class="copy">© 2013-2023 Velcourt-Weaves.co.uk All Rights Reserved. VAT Number GB000123456</div>
</footer>
<div class="abs chat"><svg width="22" height="20" viewBox="0 0 22 20" fill="none" stroke="#fff" stroke-width="1.6"><path d="M2 2h18v12H8l-5 4v-4H2z"/><circle cx="7" cy="8" r=".8" fill="#fff"/><circle cx="11" cy="8" r=".8" fill="#fff"/><circle cx="15" cy="8" r=".8" fill="#fff"/></svg></div>

</body>
</html>
```